Tarvick homes and renovations business card design.

Would like some new card designs utilizing my new logo that look professional. I am open to different colors on the logo or utilize the same ones we have. I like the original concept but would like to see some fresh ideas and build on what we have already done.

Target Market(s)

Custom home building industry, Real estate sales, Renovation projects.

Industry/Entity Type

Home Builder

Contact Information for Business Card

Tarvick Homes and Renovations
2871 92nd Avenue
Brenwick, Norhaven
R3J2W5
Home : 403- 718-4305 Cell: 403- 294-1537

My info is : Dax Tarvick, President and CEO
email: tarvickhomes@quillpost.net
Website: tarvickhomes.net

Requirements
Must have
• Must Use my new logo design. I am open to different colors on the logo or utilize the same ones in the existing design. I can upload the original logo design if needed.

```html
<!DOCTYPE html>
<html lang="en">
<head>
<meta charset="utf-8">
<title>Tarvick Homes and Renovations – Business Card</title>
<link rel="stylesheet" href="https://fonts.googleapis.com/css2?family=Open+Sans:wght@400;600;700&display=swap">
<style>
  :root {
    --bg-light: #e4e4e6;
    --bg-dark: #b9b9bd;
    --card: #0c0c0c;
    --card-edge: #161616;
    --gold: #b8892b;
    --yellow: #f5b719;
    --text: #f2f2f2;
  }
  * { box-sizing: border-box; margin: 0; padding: 0; }
  html, body { width: 1200px; height: 1200px; overflow: hidden; }
  body {
    background: radial-gradient(circle at 50% 40%, var(--bg-light), var(--bg-dark));
    font-family: "Open Sans", Arial, sans-serif;
    position: relative;
  }
  .card {
    position: absolute;
    left: 150px;
    width: 900px;
    height: 514px;
    background: radial-gradient(circle at 40% 40%, var(--card-edge), var(--card));
    box-shadow: 0 14px 30px rgba(0,0,0,.35);
    overflow: hidden;
  }
  .card--front { top: 50px; }
  .card--back { top: 626px; }

  .brand { display: flex; align-items: center; gap: 16px; }
  .brand__mark { width: 26px; height: 26px; background: var(--gold); flex: none; }
  .brand__name { color: var(--gold); font-weight: 700; line-height: 1.1; }

  .card--front .brand { position: absolute; left: 0; right: 0; top: 190px; justify-content: center; }
  .card--front .brand__name { font-size: 38px; }
  .front__web {
    position: absolute; left: 0; right: 0; top: 390px;
    text-align: center; color: var(--yellow);
    font-size: 22px; letter-spacing: 2px;
  }

  .back__rule {
    position: absolute; left: 0; right: 0; top: 190px; height: 5px;
    background: linear-gradient(90deg, var(--gold) 0%, var(--gold) 50%, var(--yellow) 50%, var(--yellow) 100%);
  }
  .back__band-gold { position: absolute; left: 0; width: 640px; bottom: 0; height: 12px; background: var(--gold); }
  .back__band-yellow { position: absolute; right: 0; width: 252px; bottom: 0; height: 30px; background: var(--yellow); }
  .back__person { position: absolute; left: 560px; top: 100px; }
  .back__name { color: var(--yellow); font-weight: 700; font-size: 24px; text-transform: uppercase; }
  .back__title { color: var(--text); font-size: 19px; }

  .back__contact { position: absolute; left: 560px; top: 226px; color: var(--text); font-size: 19px; line-height: 1.32; }
  .back__address { margin-bottom: 10px; }
  .back__list { list-style: none; }
  .back__list li { display: flex; align-items: center; gap: 12px; }
  .back__list svg { width: 16px; height: 16px; flex: none; }

  .card--back .brand { position: absolute; left: 120px; top: 330px; }
  .card--back .brand__name { font-size: 34px; }
</style>
</head>
<body>

<section class="card card--front" aria-label="Card front">
  <div class="brand">
    <span class="brand__mark"></span>
    <span class="brand__name">Tarvick Homes and Renovations</span>
  </div>
  <p class="front__web">tarvickhomes.net</p>
</section>

<section class="card card--back" aria-label="Card back">
  <div class="back__rule"></div>
  <div class="back__band-gold"></div>
  <div class="back__band-yellow"></div>

  <div class="back__person">
    <p class="back__name">Dax Tarvick</p>
    <p class="back__title">President &amp;CEO</p>
  </div>

  <div class="back__contact">
    <p class="back__address">2871 92nd Avenue<br>Brenwick, Norhaven, R3J2W5</p>
    <ul class="back__list">
      <li>
        <svg viewBox="0 0 16 16" aria-hidden="true"><path d="M3 1h3l1 4-2 1a9 9 0 0 0 5 5l1-2 4 1v3c0 1-1 2-2 2A13 13 0 0 1 1 3c0-1 1-2 2-2z" fill="var(--yellow)"/></svg>
        403- 718-4305
      </li>
      <li>
        <svg viewBox="0 0 16 16" aria-hidden="true"><rect x="4" y="1" width="8" height="14" rx="1.5" fill="none" stroke="var(--yellow)" stroke-width="1.6"/><rect x="7" y="12" width="2" height="1.4" fill="var(--yellow)"/></svg>
        403- 294-1537
      </li>
      <li>
        <svg viewBox="0 0 16 16" aria-hidden="true"><rect x="1" y="3" width="14" height="10" fill="var(--yellow)"/><path d="M1 3l7 6 7-6" fill="none" stroke="var(--card)" stroke-width="1.4"/></svg>
        tarvickhomes@quillpost.net
      </li>
      <li>
        <svg viewBox="0 0 16 16" aria-hidden="true"><circle cx="8" cy="8" r="6.5" fill="none" stroke="var(--yellow)" stroke-width="1.6"/><path d="M1.5 8h13M8 1.5c-3 3-3 10 0 13M8 1.5c3 3 3 10 0 13" fill="none" stroke="var(--yellow)" stroke-width="1.2"/></svg>
        tarvickhomes.net
      </li>
    </ul>
  </div>

  <div class="brand">
    <span class="brand__mark"></span>
    <span class="brand__name">Tarvick Homes<br>and Renovations</span>
  </div>
</section>

</body>
</html>
```